Water Filter Company Needs Bizz Cards!!

Need business cards for my company. We sell whole home water filters and salt free water softeners. No more buying bottled water. Our filtering units filter out all heavy metals, chlorine, and VOC's, last 15 years, and are maintenance free and supply your whole home with spring quality alkaline water. Our Salt free water conditioners, eliminate hard water and scale, without lowering the ph, or TDS's (total Dissolved solids)

I think this is the color code we are using on my site. My logo looks good behind it. #192841

Website will be www.Brevonix.com

Industry/Entity Type

Water Purification

Contact Information for Business Card

For now, just insert standard Dummy text. I need these text lines for the info to be editable so i can make them for multiple employees. I do have Photoshop and illustrator, unless there is a simpler program i can use solely for biz cards

Font styles to use
Sans Serif

Requirements
Must have
• Use my preexisting logo.

www.BrevoNix.com

Spring Quality Alkaline Water at every tap.

List out services. Whole Home Water Filters, Salt Free Water Softeners, Quendamar TX7, UV Sterilizers
Nice to have
• I think this is the color code we are using on my site. My logo looks good behind it. #192841 or black. Please no white or light blue backgrounds.

Maybe a picture of my tank.

Slogan like Spring Quality Alkaline Water at every tap.
And just list the services Whole Home Water Filters, Salt Free Water Softeners, Quendamar TX7, UV Sterilizers

I think I would like to not have a contrasting textured logo like I see on some of them. I may use it for my personal cards, but new employees may not want the extra expense.
Should not have
• A different logo than the one provided.

White or baby blue backgrounds. Use the color code, or blacks.

```html
<!DOCTYPE html>
<html lang="en">
<head>
<meta charset="utf-8">
<title>Brevonix Business Card</title>
<link href="https://fonts.googleapis.com/css2?family=Montserrat:wght@400;500;700&display=swap" rel="stylesheet">
<style>
  :root {
    --navy: #192841;
    --navy-panel: #22345a;
    --blue: #3bbdea;
    --text-light: #e3e6ee;
    --text-soft: #b9c3d6;
    --page: #e6e7ea;
    --white: #ffffff;
  }
  * { box-sizing: border-box; margin: 0; padding: 0; }
  html, body {
    width: 1189px; height: 1200px; overflow: hidden;
    background: var(--page);
    font-family: "Montserrat", sans-serif;
  }
  .card {
    position: absolute; left: 170px; width: 850px; height: 484px;
    border-radius: 30px; overflow: hidden;
    background: var(--navy);
    box-shadow: 0 6px 18px rgba(0,0,0,.18);
  }
  .card-front { top: 112px; }
  .card-back { top: 641px; }
  .card-strip {
    position: absolute; left: 0; right: 0; bottom: 0; height: 14px;
    background: var(--blue);
  }
  .brand { display: flex; align-items: center; gap: 14px; }
  .brand-dot { border-radius: 50%; background: var(--blue); flex: none; }
  .brand-name { font-weight: 700; color: var(--blue); letter-spacing: -1px; }

  .card-front .brand { position: absolute; left: 56px; top: 78px; }
  .card-front .brand-dot { width: 58px; height: 58px; }
  .card-front .brand-name { font-size: 78px; line-height: 1; }

  .person { position: absolute; left: 52px; top: 236px; color: var(--text-light); }
  .person-name { font-size: 29px; font-weight: 700; color: var(--blue); line-height: 1.1; }
  .person-role { font-size: 20px; font-weight: 500; margin-top: 2px; }
  .person-address { font-size: 20px; line-height: 1.3; margin-top: 16px; }
  .contact-list { list-style: none; margin-top: 12px; }
  .contact-list li { display: flex; align-items: center; gap: 8px; font-size: 20px; line-height: 27px; }
  .contact-icon { width: 20px; height: 20px; flex: none; }

  .product-image {
    position: absolute; left: 78px; top: 62px; width: 112px; height: 342px;
    border-radius: 10px;
    background: linear-gradient(180deg, #d9dadc 0%, #b9bbbe 60%, #2a2b2e 100%);
  }
  .offer-panel {
    position: absolute; left: 268px; top: 37px; width: 547px; height: 416px;
    border-radius: 22px;
    background: var(--navy-panel);
    color: var(--white);
  }
  .offer-title {
    margin-top: 22px; text-align: center;
    font-size: 30px; font-weight: 700; line-height: 40px;
  }
  .hours {
    margin: 18px auto 0; width: 483px; height: 60px; border-radius: 18px;
    background: var(--blue); color: var(--white);
    display: flex; flex-direction: column; justify-content: center; align-items: center;
    font-size: 19px; font-weight: 500; line-height: 24px;
  }
  .slogan {
    margin-top: 14px; text-align: center;
    font-size: 17px; font-weight: 700; color: var(--blue);
  }
  .services {
    list-style: none; margin: 8px auto 0; width: 470px;
    display: flex; flex-wrap: wrap; justify-content: center; gap: 4px 18px;
    font-size: 14px; font-weight: 500; color: var(--text-soft); line-height: 20px;
  }
  .services li::before { content: "✓ "; color: var(--blue); }
  .offer-footer {
    position: absolute; left: 30px; right: 30px; bottom: 20px;
    display: flex; justify-content: space-between; align-items: flex-end;
  }
  .offer-footer .brand-dot { width: 34px; height: 34px; }
  .offer-footer .brand-name { font-size: 46px; line-height: 1; }
  .social { display: flex; flex-direction: column; align-items: flex-end; gap: 6px; }
  .social-list { display: flex; gap: 15px; list-style: none; margin-right: 14px; }
  .social-list li { width: 28px; height: 28px; border-radius: 4px; background: var(--blue); }
  .site { font-size: 19px; font-weight: 500; color: var(--text-light); }
</style>
</head>
<body>

<section class="card card-front">
  <div class="brand">
    <span class="brand-dot"></span>
    <span class="brand-name">Brevonix</span>
  </div>
  <div class="person">
    <h1 class="person-name">DANIEL REYES</h1>
    <p class="person-role">Manager</p>
    <p class="person-address">42 Harbor Lane,<br>Cedar Falls, IA</p>
    <ul class="contact-list">
      <li>
        <svg class="contact-icon" viewBox="0 0 20 20"><circle cx="10" cy="10" r="9" fill="none" stroke="#3bbdea" stroke-width="2"/><path d="M7 5.5l2 2-1 1.2c.6 1.4 1.6 2.4 3 3l1.2-1 2 2-1.2 1.5C9.5 14 6 10.5 5.6 6.7z" fill="#3bbdea"/></svg>
        1 555 014 2290
      </li>
      <li>
        <svg class="contact-icon" viewBox="0 0 20 20"><circle cx="10" cy="10" r="9" fill="none" stroke="#3bbdea" stroke-width="2"/><rect x="5.5" y="6.5" width="9" height="7" fill="none" stroke="#3bbdea" stroke-width="1.5"/><path d="M5.5 6.5l4.5 4 4.5-4" fill="none" stroke="#3bbdea" stroke-width="1.5"/></svg>
        hello@brevonix.com
      </li>
      <li>
        <svg class="contact-icon" viewBox="0 0 20 20"><circle cx="10" cy="10" r="9" fill="none" stroke="#3bbdea" stroke-width="2"/><circle cx="10" cy="10" r="5" fill="none" stroke="#3bbdea" stroke-width="1.3"/><path d="M5 10h10M10 5v10" stroke="#3bbdea" stroke-width="1.3"/></svg>
        www.brevonix.com
      </li>
    </ul>
  </div>
  <div class="card-strip"></div>
</section>

<section class="card card-back">
  <div class="product-image" role="img" aria-label="Photo of a UV water sterilizer unit with its control box"></div>
  <div class="offer-panel">
    <h2 class="offer-title">WHOLE HOME<br>WATER FILTERS FOR THE<br>BEST PRICE</h2>
    <div class="hours">
      <span>Monday – Saturday: 8am – 9pm</span>
      <span>Sunday: 9am – 10pm</span>
    </div>
    <p class="slogan">Spring Quality Alkaline Water at every tap.</p>
    <ul class="services">
      <li>Whole Home Water Filters</li>
      <li>Salt Free Water Softeners</li>
      <li>Quendamar TX7</li>
      <li>UV Sterilizers</li>
    </ul>
    <div class="offer-footer">
      <div class="brand">
        <span class="brand-dot"></span>
        <span class="brand-name">Brevonix</span>
      </div>
      <div class="social">
        <ul class="social-list" aria-label="Social media">
          <li></li><li></li><li></li><li></li>
        </ul>
        <span class="site">www.BrevoNix.com</span>
      </div>
    </div>
  </div>
  <div class="card-strip"></div>
</section>

</body>
</html>
```